Business card (AI file uploaded)

We need a business card design that is minimalist using existing logo (attached). Source files must be editable so we can make the same design with other names.

Screenshots included of a design I was working on to give you an idea of the style I would like. Looking for similar modern styles

Thanks

```html
<!DOCTYPE html>
<html lang="en">
<head>
<meta charset="utf-8">
<title>Delane Law Group – Business Card</title>
<link href="https://fonts.googleapis.com/css2?family=Arimo:wght@400;700&display=swap" rel="stylesheet">
<style>
  :root {
    --stage: #cfd6d8;
    --card-black: #1b1b1b;
    --card-band: #2a2a2a;
    --card-white: #ffffff;
    --card-grey: #eeeeee;
    --ink-light: #f2f2f2;
    --ink-muted: #b9b9b9;
    --ink-dark: #1a1a1a;
    --ink-soft: #3a3a3a;
  }
  * { margin: 0; padding: 0; box-sizing: border-box; }
  html, body {
    width: 1200px; height: 1000px; overflow: hidden;
    background: var(--stage);
    font-family: "Arimo", Arial, sans-serif;
  }
  .stage {
    position: relative; width: 1200px; height: 1000px;
  }
  .card {
    position: absolute; left: 250px;
    width: 700px; height: 400px;
    overflow: hidden;
    box-shadow: 0 10px 30px rgba(0,0,0,0.25);
  }
  /* front */
  .card-front { top: 60px; background: var(--card-black); }
  .card-front .top-band {
    position: absolute; inset: 0;
    width: 700px; height: 400px;
  }
  .attorney {
    position: absolute; right: 44px; top: 34px; text-align: right;
    color: var(--ink-light);
  }
  .attorney-name { font-size: 27px; font-weight: 700; }
  .attorney-title { font-size: 12px; margin-top: 6px; color: var(--ink-light); }
  .firm-mark {
    position: absolute; left: 42px; top: 150px;
    display: flex; align-items: center; gap: 22px;
  }
  .firm-mark .dot {
    width: 96px; height: 96px; border-radius: 50%;
    border: 6px solid var(--ink-light);
  }
  .firm-name {
    color: var(--ink-light); font-size: 38px; font-weight: 400;
    letter-spacing: 3px; text-transform: uppercase; line-height: 1.15;
  }
  .practice-areas {
    position: absolute; left: 40px; bottom: 36px;
    color: var(--ink-muted); font-size: 18px; word-spacing: 2px;
  }
  /* back */
  .card-back { top: 540px; background: var(--card-white); }
  .card-back .lower-band {
    position: absolute; left: 0; right: 0; top: 185px; bottom: 0;
    background: var(--card-grey);
  }
  .back-mark {
    position: absolute; left: 0; right: 0; top: 36px;
    display: flex; flex-direction: column; align-items: center; gap: 14px;
  }
  .back-mark .dot {
    width: 90px; height: 90px; border-radius: 50%;
    border: 6px solid var(--ink-dark);
  }
  .back-mark .firm-name { color: var(--ink-dark); font-size: 20px; letter-spacing: 2px; }
  .contact {
    position: absolute; left: 0; right: 0; top: 222px;
    text-align: center; color: var(--ink-dark); font-size: 19px; line-height: 1.45;
    letter-spacing: 0.5px;
  }
  .contact-line { display: flex; justify-content: center; align-items: center; gap: 8px; }
  .contact-line svg { width: 20px; height: 16px; }
  .gap { display: inline-block; width: 14px; }
</style>
</head>
<body>
<main class="stage">

  <section class="card card-front" aria-label="Business card front">
    <svg class="top-band" viewBox="0 0 700 400" aria-hidden="true">
      <polygon points="0,0 700,0 700,205 0,235" fill="#2a2a2a"/>
    </svg>
    <div class="attorney">
      <p class="attorney-name">Marcus Delane</p>
      <p class="attorney-title">Attorney At Law</p>
    </div>
    <div class="firm-mark">
      <span class="dot"></span>
      <p class="firm-name">Delane<br>Law Group PC</p>
    </div>
    <p class="practice-areas">Real Estate &nbsp;|&nbsp; Bankruptcy &nbsp;|&nbsp; Social Security Disability</p>
  </section>

  <section class="card card-back" aria-label="Business card back">
    <div class="lower-band"></div>
    <div class="back-mark">
      <span class="dot"></span>
      <p class="firm-name">Delane Law Group PC</p>
    </div>
    <div class="contact">
      <p>410 Harbor Ave. Suite 200, Lakemont, IL 60100</p>
      <p class="contact-line">
        <svg viewBox="0 0 20 16" aria-hidden="true"><rect x="3" y="1" width="9" height="14" rx="2" fill="none" stroke="#1a1a1a" stroke-width="1.5"/><path d="M15 5q2 3 0 6" fill="none" stroke="#1a1a1a" stroke-width="1.3"/></svg>
        P: 555.014.2280<span class="gap"></span>F: 555.014.2291
      </p>
      <p class="contact-line">
        <svg viewBox="0 0 20 16" aria-hidden="true"><rect x="1" y="2" width="18" height="12" fill="none" stroke="#1a1a1a" stroke-width="1.5"/><path d="M1 2l9 7 9-7" fill="none" stroke="#1a1a1a" stroke-width="1.5"/></svg>
        info@delanelaw.com
      </p>
    </div>
  </section>

</main>
</body>
</html>
```